Whitening Pen artwork design

Whitening Pens with silkscreen printing:
sample: https://www.shopvarnel.com/Korimo-Whitening-Carbamide-Sensitivity-Travel-Friendly/dp/Q48T2K9X5R/ref=sr_1_5?dchild=1&keywords=whitening+pen&qid=1615425398&sr=8-5

inside the writing:
"teeth whitening pen " change to "FARO WHITENING PEN"
"logo" change to our logo

requirements:
Inches: 1.77" wide x 1.57" around
CM: 4.5cm wide x 4cm around

See attached file Generic Pen Artwork Placement Silkscreen – this is not a template, just a guideline, refer to the exact sizing above

- An "identifying marker" is required: Teeth Whitening Pen or Teeth Whitening Gel (for example)

-We require PDF files created to print ready specifications. Color images should be down-sampled to 300DPI

-Please provide us your Hueledger color reference for the color used in your artwork

https://www.hueledger.com/color-finder#/pick?hueBook=hueSolidCoatedV3M2

-Please ensure that all fonts are embedded in the PDF document or make sure you convert fonts to outlines to prevent any issues with fonts (AI-Type-Create Outlines)

We will need your print ready artwork in a high resolution PDF file

```html
<!DOCTYPE html>
<html lang="en">
<head>
<meta charset="utf-8">
<title>FARO Whitening Pen Artwork</title>
<link rel="stylesheet" href="https://fonts.googleapis.com/css2?family=Montserrat:wght@300;500;600&display=swap">
<style>
  :root {
    --ink: #464a4e;
    --blush: #e8aa9c;
    --paper: #ffffff;
    --frost: #eef1f4;
    --frost-deep: #d7dde3;
  }
  * { margin: 0; padding: 0; box-sizing: border-box; }
  html, body { width: 1200px; height: 1200px; overflow: hidden; background: var(--paper); }
  .canvas { position: relative; width: 1200px; height: 1200px; font-family: "Montserrat", sans-serif; }

  .vertical { writing-mode: vertical-rl; white-space: nowrap; }

  /* Carton */
  .carton {
    position: absolute; left: 181px; top: 32px; width: 252px; height: 1134px;
    background: var(--paper); box-shadow: 0 0 0 1px #e6e6e6;
  }
  .carton__band {
    position: absolute; left: 0; top: 0; width: 85px; height: 100%;
    background: var(--ink);
  }
  .carton__tagline {
    position: absolute; left: 24px; top: 48px;
    color: var(--blush); font-weight: 300; font-size: 27px; letter-spacing: 0.5px;
  }
  .carton .badge { left: 166px; top: 60px; }
  .carton .brand-dot { left: 126px; top: 202px; width: 70px; height: 70px; }
  .carton .brand-name { left: 116px; top: 310px; font-size: 104px; letter-spacing: 14px; }

  /* Pens */
  .pen {
    position: absolute; top: 50px; width: 104px; height: 1106px; border-radius: 14px;
    background: linear-gradient(90deg, var(--frost-deep), var(--frost) 30%, #fbfcfd 55%, var(--frost-deep));
  }
  .pen--one { left: 478px; }
  .pen--two { left: 630px; }

  /* Flat silkscreen label */
  .label .badge { left: 998px; top: 206px; width: 48px; height: 72px; }
  .label .badge span { font-size: 16px; }
  .label .brand-dot { left: 978px; top: 318px; width: 56px; height: 56px; }
  .label .brand-name { left: 960px; top: 400px; font-size: 90px; letter-spacing: 12px; }
  .label__marker {
    position: absolute; left: 904px; top: 390px;
    color: var(--blush); font-weight: 300; font-size: 38px; letter-spacing: 1px;
  }

  /* Shared marks */
  .badge {
    position: absolute; width: 58px; height: 90px;
    background: var(--blush); border-radius: 50% 50% 50% 50% / 40% 40% 60% 60%;
    display: flex; align-items: center; justify-content: center;
  }
  .badge span { writing-mode: vertical-rl; color: var(--ink); font-weight: 600; font-size: 20px; }
  .brand-dot { position: absolute; border-radius: 50%; background: var(--blush); }
  .brand-name { position: absolute; color: var(--ink); font-weight: 500; line-height: 1; }
</style>
</head>
<body>
<main class="canvas">
  <section class="carton">
    <div class="carton__band"></div>
    <p class="carton__tagline vertical">FARO WHITENING PEN · Professional Level Whitening Guaranteed</p>
    <div class="badge"><span>NEW</span></div>
    <div class="brand-dot"></div>
    <p class="brand-name vertical">SOLANE</p>
  </section>

  <div class="pen pen--one" role="img" aria-label="Clear whitening pen with brush tip and printed brand artwork"></div>
  <div class="pen pen--two" role="img" aria-label="Second clear whitening pen with brush tip and printed brand artwork"></div>

  <section class="label">
    <div class="badge"><span>NEW</span></div>
    <div class="brand-dot"></div>
    <p class="brand-name vertical">SOLANE</p>
    <p class="label__marker vertical">FARO WHITENING PEN</p>
  </section>
</main>
</body>
</html>
```